Fahrzeugbeschriftung für Elektrotechnik-Betrieb
Zielgruppe
Unser Kunde ist ein Heizung und Sanitär Betrieb mit Sitz in Hamburg. Zu uns kamen sie mit dem Wunsch nach einer Webseite für Ihren Imageaufbau und Mitarbeitersuche. Der Meisterbetrieb beschäftigt sich mit Heizung und hochwertigen exklusiven Bädern.
Die Domain der aktuellen Webseite: brunner-waerme.de
Adresse: Holderbachweg 14, 54528 Kastelheim
Telefonnummer: 06573 817360
Bitte das Design beachten, sonst gerne kreativ und auffällig! Im Vordergrund stehen die zwei Themenbereiche Bäder und Heizung und zusätzlich die Mitarbeitersuche. Beispielbilder im Anhang! (Das alte Autodesign befindet sich auch im Anhang)
Aufgabenstellung
Der Kunde hätte das Autodesign gerne auffällig und modern. Im Fokus stehen die Leistungen (Heizung und Bäder) und die Mitarbeitersuche. Ebenfalls sollen Logo (befindet sich im Anhang), Telefonnummer und Webseite klar zu sehen sein.
Nähere Vorgaben:
-Vorne: nur das Logo
-Seiten: Thema Bad und Heizung, Aufruf zur Mitarbeitersuche, Logo, Telefonnummer, Webseite
-Hinten: Logo (groß/oben); Telefonnummer und Webseite (rechts), Aufruf zur Mitarbeitersuche (links)
Unsere Idee: Aufteilung der Themen Bäder und Heizung
1. auf der einen Seite des Autos Thema “Bäder”(blau aus Logo) - Der Kunde möchte hochwertige Bäder verkaufen!
Bsp.:“Dein Partner rund um deine exklusive Wellnessoase”
Mitarbeitersuche: “Bei uns fühlst auch du dich wohl/Nicht nur die Kunden fühlen sich bei uns wohl. Bewirb dich jetzt! “
Bitte mit Bildern arbeiten! Ein schönes Badezimmer mit lächelnden Menschen. Stockfotos bitte passend farblich anpassen.
Beispiel Stockfotos:
- https://www.bildarchivplus.example/de/image-photo/happy-laughing-asian-woman-shaving-her-100000001
- https://www.bildarchivplus.example/de/image-photo/portrait-young-happy-couple-getting-ready-100000002
- https://www.bildarchivplus.example/de/image-photo/couple-facing-bathroom-drawing-gradating-photo-100000003
- https://www.bildarchivplus.example/de/image-photo/morning-sexy-couple-muscular-man-bath-100000004
2. und auf der anderen Seite Thema “Heizung”(orange aus Logo)
Bsp.:“Wir sorgen auch für dein perfektes Wohlfühlklima”
Mitarbeitersuche: “Bei uns fühlst auch du dich wohl/Nicht nur die Kunden fühlen sich bei uns wohl. Bewirb dich jetzt!”
Bitte mit Bildern arbeiten! Ein passendes Bild mit fröhlicher Familie. Stockfotos bitte passend farblich anpassen.
- https://www.bildarchivplus.example/de/image-photo/floor-heating-young-woman-walking-house-100000005
- https://www.bildarchivplus.example/de/image-illustration/heating-concept-un..

```html
<!DOCTYPE html>
<html lang="de">
<head>
<meta charset="utf-8">
<title>Brunner Haustechnik – Fahrzeugbeschriftung</title>
<link rel="stylesheet" href="https://fonts.googleapis.com/css2?family=Roboto+Condensed:wght@400;700&display=swap">
<style>
:root{
  --orange:#ef7d33;
  --orange-light:#f6a033;
  --blue:#00a3dd;
  --blue-light:#3fbded;
  --grey:#575757;
  --page:#e9e9e9;
  --panel:#ffffff;
  --body-grey:#d9dadc;
  --ink:#1e1e1e;
  --halo:0 0 2px #fff,0 0 2px #fff,1px 1px 0 #fff,-1px -1px 0 #fff,1px -1px 0 #fff,-1px 1px 0 #fff;
}
*{margin:0;padding:0;box-sizing:border-box}
html,body{width:706px;height:1200px;overflow:hidden;background:var(--page)}
body{position:relative;font-family:"Roboto Condensed",sans-serif;font-weight:700}
.panel{position:absolute;overflow:hidden;border-radius:14px;background:var(--panel)}
.panel svg{position:absolute;left:0;top:0}
.photo{position:absolute}
.txt{position:absolute;white-space:nowrap;line-height:1.05}
.recruit{font-size:10.5px}
.haloed{text-shadow:var(--halo)}
.brand{position:absolute;display:flex;align-items:center;gap:8px;color:var(--grey)}
.brand .mark{background:var(--orange);flex:none}
.brand .name{line-height:.9;letter-spacing:-.5px}
.brand .name span{display:block}
.address{font-size:7px;line-height:1.2}
.swatch{position:absolute;width:50px;height:50px}
.cmyk{position:absolute;font-size:11.5px;line-height:13.5px;color:var(--ink);font-weight:400}
</style>
</head>
<body>

<!-- Heizung side -->
<section class="panel side-heating" style="left:18px;top:55px;width:670px;height:240px">
  <div class="photo" role="img" aria-label="Fußbodenheizung mit Heizschlangen und digitalem Raumthermostat auf Holzboden"
       style="left:230px;top:0;width:390px;height:240px;background:linear-gradient(160deg,#e8d9c8 0%,#d9b89a 45%,#c98e62 100%)"></div>
  <svg width="670" height="240" viewBox="0 0 670 240" aria-hidden="true">
    <path d="M575 0 H670 V240 H380 C470 215 560 200 600 165 Z" fill="var(--orange)"/>
    <path d="M575 0 L590 0 L590 140 Q560 170 520 180 Z" fill="var(--orange)" opacity=".55"/>
  </svg>
  <div class="txt recruit" style="left:296px;top:15px;color:var(--orange)">Nicht nur die Kunden fühlen sich bei uns wohl. Bewirb dich jetzt!</div>
  <div class="brand" style="left:430px;top:58px">
    <span class="mark" style="width:44px;height:44px"></span>
    <span class="name"><span style="font-size:46px">brunner</span><span style="font-size:31px">haustechnik</span></span>
  </div>
  <div class="txt" style="left:510px;top:146px;font-size:12px;color:#fff;line-height:1.15">Wir sorgen auch für dein<br>perfektes Wohlfühlklima.</div>
  <div class="txt address" style="left:152px;top:152px;color:var(--orange)">Brunner GmbH<br>Holderbachweg 14<br>54528 Kastelheim</div>
  <div class="txt" style="left:174px;top:192px;font-size:15px;color:var(--orange)">Tel. 06573 817360</div>
  <div class="txt" style="left:304px;top:190px;font-size:15px;color:var(--orange)">www.brunner-waerme.de</div>
</section>

<!-- Bad side -->
<section class="panel side-bath" style="left:18px;top:428px;width:670px;height:240px">
  <div class="photo" role="img" aria-label="Helles Badezimmer mit Badewanne, lächelnder Mann im Schaumbad und Frau im Bademantel"
       style="left:95px;top:0;width:365px;height:240px;background:linear-gradient(120deg,#c9b6a4 0%,#e6e2dc 45%,#f3f1ee 100%)"></div>
  <svg width="670" height="240" viewBox="0 0 670 240" aria-hidden="true">
    <path d="M0 0 H110 C95 70 100 130 140 165 C180 195 230 225 290 240 H0 Z" fill="var(--blue)"/>
    <path d="M0 0 H40 V240 H0 Z" fill="var(--blue-light)" opacity=".6"/>
  </svg>
  <div class="txt recruit" style="left:128px;top:17px;color:var(--blue)">Nicht nur die Kunden fühlen sich bei uns wohl. Bewirb dich jetzt!</div>
  <div class="brand" style="left:42px;top:42px">
    <span class="mark" style="width:44px;height:44px"></span>
    <span class="name"><span style="font-size:46px">brunner</span><span style="font-size:31px">haustechnik</span></span>
  </div>
  <div class="txt haloed" style="left:40px;top:140px;font-size:14px;color:var(--blue);line-height:1.15">Dein Partner rund um deine<br>exklusive Wellnessoase.</div>
  <div class="txt" style="left:206px;top:196px;font-size:15px;color:var(--blue)">Tel. 06573 817360</div>
  <div class="txt" style="left:332px;top:196px;font-size:15px;color:var(--blue)">www.brunner-waerme.de</div>
  <div class="txt address" style="left:470px;top:156px;color:var(--blue)">Brunner GmbH<br>Holderbachweg 14<br>54528 Kastelheim</div>
</section>

<!-- Front -->
<section class="panel front" style="left:40px;top:770px;width:290px;height:285px;background:var(--body-grey)">
  <div class="brand" style="left:84px;top:122px">
    <span class="mark" style="width:26px;height:26px"></span>
    <span class="name"><span style="font-size:21px">brunner</span><span style="font-size:14px">haustechnik</span></span>
  </div>
</section>

<!-- Rear -->
<section class="panel rear" style="left:408px;top:770px;width:272px;height:285px;background:var(--body-grey)">
  <div class="brand" style="left:34px;top:22px">
    <span class="mark" style="width:60px;height:60px"></span>
    <span class="name"><span style="font-size:52px">brunner</span><span style="font-size:33px">haustechnik</span></span>
  </div>
  <div class="txt" style="left:24px;top:138px;font-size:7px;color:var(--orange);line-height:1.25">Nicht nur die Kunden fühlen sich bei uns wohl.<br>Bewirb dich jetzt!</div>
  <div class="txt" style="right:14px;top:178px;font-size:15px;color:var(--grey)">Tel. 06573 817360</div>
  <div class="txt" style="right:14px;top:200px;font-size:15px;color:var(--grey)">www.brunner-waerme.de</div>
</section>

<!-- Colour swatches -->
<div class="swatch" style="left:14px;top:1084px;background:var(--orange)"></div>
<div class="cmyk" style="left:82px;top:1080px">C:&nbsp;&nbsp;0<br>M: 65<br>I:&nbsp;&nbsp;90<br>K:&nbsp;&nbsp;0</div>
<div class="swatch" style="left:14px;top:1148px;background:var(--orange-light)"></div>
<div class="cmyk" style="left:82px;top:1144px">C:&nbsp;&nbsp;0<br>M: 45<br>I:&nbsp;&nbsp;90<br>K:&nbsp;&nbsp;0</div>
<div class="swatch" style="left:318px;top:1086px;background:var(--blue)"></div>
<div class="cmyk" style="left:393px;top:1083px">C: 85<br>M:&nbsp;&nbsp;0<br>I :&nbsp;&nbsp;0<br>K: 10</div>
<div class="swatch" style="left:318px;top:1150px;background:var(--blue-light)"></div>
<div class="cmyk" style="left:393px;top:1147px">C: 65<br>M:&nbsp;&nbsp;0<br>I :&nbsp;&nbsp;0<br>K:&nbsp;&nbsp;5</div>
<div class="swatch" style="left:590px;top:1086px;background:var(--grey)"></div>
<div class="cmyk" style="left:645px;top:1083px">C:&nbsp;&nbsp;0<br>M:&nbsp;&nbsp;0<br>I :&nbsp;&nbsp;0<br>K: 80</div>

</body>
</html>
```